Corvath Holdings, LLC

We are a design build general contracting company.
We work with commercial accounts and private developers. We build retail spaces, restaurants and housing projects.
Im looking for a clean professional type of logo incorporating a roman flavor, think ionic columns and pedestals.
Two toned colorway.
I like unusual fonts and Im not afraid to do something bold with the logo.
Contact Information for Business Card
Marisol Brenkowitz
318-472-9051 corvathmb@mailvexo.com
Font styles to use
Decorative
Colors
Designer to choose colors to be used in the design.
Requirements
Should not have
- I don't like reds pinks.

```html
<!DOCTYPE html>
<html lang="en">
<head>
<meta charset="utf-8">
<title>Corvath Holdings – Business Card</title>
<link rel="stylesheet" href="https://fonts.googleapis.com/css2?family=Source+Serif+4:opsz,wght@8..60,400;8..60,500&display=swap">
<style>
  :root {
    --card-black: #000000;
    --gold: #d9a441;
    --column-light: #3c3c3c;
    --column-dark: #1e1e1e;
  }
  html, body {
    margin: 0;
    padding: 0;
    width: 1200px;
    height: 686px;
    overflow: hidden;
    background: var(--card-black);
  }
  .business-card {
    position: relative;
    width: 1200px;
    height: 686px;
    background: var(--card-black);
    overflow: hidden;
    font-family: "Source Serif 4", Georgia, serif;
    color: var(--gold);
  }
  .column-placeholder {
    position: absolute;
    top: 0;
    width: 112px;
    height: 686px;
  }
  .column-placeholder--left {
    left: 0;
    background: linear-gradient(to right, var(--column-light), var(--column-dark));
  }
  .column-placeholder--right {
    right: 0;
    background: linear-gradient(to left, var(--column-light), var(--column-dark));
  }
  .brand {
    position: absolute;
    left: 0;
    right: 0;
    margin: 0;
    text-align: center;
    font-weight: 400;
    line-height: 1;
  }
  .brand__name {
    top: 135px;
    font-size: 140px;
    letter-spacing: 3px;
  }
  .brand__tagline {
    top: 282px;
    font-size: 66px;
    letter-spacing: 1px;
  }
  .contact {
    position: absolute;
    top: 378px;
    left: 0;
    right: 0;
    text-align: center;
    font-size: 46px;
    line-height: 56px;
    font-weight: 400;
  }
  .contact p { margin: 0; }
</style>
</head>
<body>
  <div class="business-card">
    <div class="column-placeholder column-placeholder--left" role="img" aria-label="Ionic column illustration"></div>
    <div class="column-placeholder column-placeholder--right" role="img" aria-label="Ionic column illustration"></div>

    <h1 class="brand brand__name">CORVATH</h1>
    <h2 class="brand brand__tagline">HOLDINGS</h2>

    <div class="contact">
      <p class="contact__name">Marisol Brenkowitz</p>
      <p class="contact__phone">318-472-9051</p>
      <p class="contact__email">corvathmb@mailvexo.com</p>
    </div>
  </div>
</body>
</html>
```